mapleridgegroup Business Card Design

Business card with logo design for mapleridgegroup. We are a group of professional project managers based on the Pareto Principle that 80% of the work is done by 20% of the people. I have a makeshift logo that uses a pi chart with 30% and 20% and the 20% pie slice is set slightly out and up. Have played around with a teal and orange colour scheme.

Industry/Entity Type

Business

Contact Information for Business Card

Gareth Pembroke
Director
mapleridgegroup

0452 803716

```html
<!DOCTYPE html>
<html lang="en">
<head>
<meta charset="utf-8">
<title>mapleridgegroup Business Card</title>
<link href="https://fonts.googleapis.com/css2?family=Montserrat:wght@300;400;700&display=swap" rel="stylesheet">
<style>
  :root {
    --stage: #dedada;
    --paper: #f4f2f2;
    --white: #ffffff;
    --orange: #e9714a;
    --teal: #2a97a3;
    --grey: #6d6e71;
    --soft-grey: #8a8a8c;
    --rule: #efb9a5;
  }
  * { margin: 0; padding: 0; box-sizing: border-box; }
  html, body { width: 1200px; height: 1000px; overflow: hidden; }
  body { font-family: "Montserrat", Arial, sans-serif; background: var(--white); }

  .stage {
    height: 687px;
    background: var(--stage);
    display: flex;
    align-items: center;
    justify-content: center;
  }
  .card {
    width: 600px;
    height: 340px;
    background: var(--paper);
    box-shadow: 0 10px 30px rgba(0,0,0,0.12);
    display: flex;
    align-items: center;
    padding: 0 40px 0 56px;
  }
  .card-brand {
    width: 170px;
    display: flex;
    align-items: center;
    gap: 8px;
  }
  .brand-dot { width: 14px; height: 14px; border-radius: 50%; background: var(--orange); flex: none; }
  .brand-name { font-size: 15px; font-weight: 400; color: var(--orange); letter-spacing: 0.2px; }
  .card-divider { width: 1px; height: 120px; background: var(--rule); margin: 0 30px 0 20px; }
  .card-details { color: var(--soft-grey); }
  .holder-name { font-size: 22px; font-weight: 700; letter-spacing: 0.5px; text-transform: uppercase; line-height: 1.1; }
  .holder-name .first { color: var(--orange); }
  .holder-name .last { color: var(--teal); }
  .holder-role { font-size: 15px; font-weight: 300; color: var(--soft-grey); margin-bottom: 12px; }
  .contact-line { font-size: 10px; font-weight: 400; line-height: 1.4; color: var(--grey); }

  .logo-row {
    height: 313px;
    display: flex;
    justify-content: space-around;
    align-items: center;
    padding: 0 150px;
  }
  .logo-lockup { display: flex; align-items: center; gap: 12px; }
  .lockup-dot { width: 26px; height: 26px; border-radius: 50%; flex: none; }
  .lockup-name { font-size: 30px; font-weight: 300; }
  .lockup-mono .lockup-dot { background: var(--grey); }
  .lockup-mono .lockup-name { color: var(--grey); }
  .lockup-colour .lockup-dot { background: var(--orange); }
  .lockup-colour .lockup-name { color: var(--orange); }
</style>
</head>
<body>
  <section class="stage">
    <article class="card">
      <div class="card-brand">
        <span class="brand-dot"></span>
        <span class="brand-name">mapleridgegroup</span>
      </div>
      <div class="card-divider"></div>
      <div class="card-details">
        <p class="holder-name"><span class="first">Gareth</span> <span class="last">Pembroke</span></p>
        <p class="holder-role">Director mapleridgegroup</p>
        <p class="contact-line">str. Name 25</p>
        <p class="contact-line">tel. 0452 803716</p>
        <p class="contact-line">hello@mapleridgegroup.com.au</p>
        <p class="contact-line">www.mapleridgegroup.com.au</p>
      </div>
    </article>
  </section>
  <section class="logo-row">
    <div class="logo-lockup lockup-mono">
      <span class="lockup-dot"></span>
      <span class="lockup-name">mapleridgegroup</span>
    </div>
    <div class="logo-lockup lockup-colour">
      <span class="lockup-dot"></span>
      <span class="lockup-name">mapleridgegroup</span>
    </div>
  </section>
</body>
</html>
```